Wordpress Theme for a Professional Speaker's Website

I I need a website to promote myself as a speaker to corporations and meeting planners. Some examples of similar sites I like are:

http://www.beginwithpurpose.example (this is by far my favorite)
http://www.tovaruskin.example
http://www.glenbeckworth.example
http://www.lomtrisel.example
http://www.dawnafterstorms.example
http://www.osricpellandine.example

I like modern, minimalistic, innovative. I'm okay if it's edgy but still want it communicate professionalism.

The primary objective is to position me as an expert who can deliver valuable information in an entertaining manner.

There are two calls to action. The first is to capture name and email address to subscribe to my newsletter. The second is to request more information about booking me to speak for their company, organization, etc.

The pages on the website will ultimately be the following:

1. Home (should include sections for recent blog posts, featured topics/presentations, short bio, testimonials, email capture, and anything else you think should be added.
2. Meet Ross
3. Blog
4. Keynotes & Speaking
5. Training & Webinars
6. Coaching & Consulting
7. Testimonials
8. Book Ross
9. Media Inquiries
10. Contact

Please feel free to use your creativity. I don't want my requirements to limit you in any way. I'm just looking for a modern, professional site that will make me stand out from the crowd.

I don't have any existing site or brand identity. My plan is to have the website design I ultimately choose serve as the foundation for the rest of my brand identity.

Target Market(s)

Corporate meeting planners and executives

Industry/Entity Type

It Professional

Font styles to use
Sans Serif

Requirements
Must have
• Email capture, testimonials, blog
Nice to have
• None
Should not have
• None

```html
<!DOCTYPE html>
<html lang="en">
<head>
<meta charset="utf-8">
<title>Ross Valdane – Testimonials</title>
<link href="https://fonts.googleapis.com/css2?family=Arimo&family=Share+Tech+Mono&display=swap" rel="stylesheet">
<style>
  :root {
    --page-bg: #ababab;
    --footer-bg: #959595;
    --card-bg: #e5e5e5;
    --navy: #034a68;
    --navy-text: #14506d;
    --accent-red: #b8360e;
    --white: #ffffff;
    --body-grey: #5a5a5a;
    --menu-grey: #5f5f5f;
    --band-text: #a9bcc7;
  }
  * { margin: 0; padding: 0; box-sizing: border-box; }
  html, body { width: 1200px; height: 1016px; overflow: hidden; }
  body { position: relative; background: var(--page-bg); font-family: "Arimo", Arial, sans-serif; }
  h2, h3, h4 { font-weight: 400; }

  .top-rule { position: absolute; left: 0; top: 0; width: 1200px; height: 2px; background: var(--white); }

  .section-title__line { position: absolute; top: 95px; height: 4px; background: var(--white); }
  .section-title__text { position: absolute; top: 82px; left: 494px; width: 206px; text-align: center; color: var(--white); font-size: 24px; font-weight: 400; letter-spacing: 0.3px; }

  .testimonial { position: absolute; top: 186px; width: 166px; height: 234px; background: var(--card-bg); }
  .testimonial__photo { position: absolute; width: 122px; height: 124px; }
  .testimonial__quote { position: absolute; top: 167px; left: 17px; width: 142px; font-size: 12px; line-height: 14.5px; color: var(--body-grey); text-align: left; }
  .testimonial__base { position: absolute; top: 420px; width: 216px; height: 8px; background: var(--navy); }

  .signup { position: absolute; left: 284px; top: 562px; width: 916px; height: 144px; background: var(--navy); }
  .signup__art { position: absolute; left: 270px; top: 530px; width: 172px; height: 130px; border-radius: 6px; background: linear-gradient(150deg, #f2f2f2 0%, #dcdcdc 45%, #c0664a 100%); }
  .signup__title { position: absolute; left: 198px; top: 20px; font-family: "Share Tech Mono", monospace; font-variant: small-caps; font-weight: 400; font-size: 23px; letter-spacing: 3.2px; color: var(--band-text); }
  .signup__field { position: absolute; left: 168px; top: 81px; width: 512px; height: 35px; background: var(--white); border: none; }
  .signup__button { position: absolute; left: 698px; top: 81px; width: 128px; height: 35px; background: var(--accent-red); color: #f3e6df; border: none; font-family: "Share Tech Mono", monospace; font-size: 16px; letter-spacing: 2px; }

  .site-footer { position: absolute; left: 0; top: 706px; width: 1200px; height: 310px; background: var(--footer-bg); }
  .footer-heading { position: absolute; top: 79px; font-family: "Share Tech Mono", monospace; font-weight: 400; font-size: 22px; letter-spacing: 2.6px; color: var(--navy-text); }
  .footer-menu { position: absolute; top: 116px; list-style: none; font-size: 16px; line-height: 19.3px; color: var(--menu-grey); }
  .social-links { position: absolute; left: 614px; top: 134px; display: flex; gap: 19px; list-style: none; }
  .social-links li { width: 12px; height: 12px; border-radius: 50%; background: var(--navy-text); }
  .contact { position: absolute; left: 840px; top: 117px; width: 282px; text-align: center; font-style: normal; font-size: 14px; line-height: 16.8px; color: var(--navy-text); }
</style>
</head>
<body>
  <div class="top-rule"></div>

  <section class="testimonials">
    <span class="section-title__line" style="left:223px;width:270px"></span>
    <h2 class="section-title__text">TESTIMONIALS</h2>
    <span class="section-title__line" style="left:700px;width:270px"></span>

    <article class="testimonial" style="left:139px">
      <div class="testimonial__photo" role="img" aria-label="Portrait of a client with long brown hair" style="left:17px;top:21px;width:120px;background:linear-gradient(160deg,#f4f1ee,#a58a72 60%,#2c2a2c)"></div>
      <p class="testimonial__quote">“Lorem ipsum dolor sit<br>&nbsp;amet, consectetur adip<br>iscing elit, sed do eiusm ”</p>
    </article>
    <article class="testimonial" style="left:387px">
      <div class="testimonial__photo" role="img" aria-label="Portrait of a client in a white shirt and tie" style="left:23px;top:21px;width:126px;background:linear-gradient(160deg,#dce3ea,#c79f86 55%,#eef1f4)"></div>
      <p class="testimonial__quote" style="left:19px">“Lorem ipsum dolor sit<br>&nbsp;amet, consectetur adip<br>iscing elit, sed do eiusm ”</p>
    </article>
    <article class="testimonial" style="left:639px">
      <div class="testimonial__photo" role="img" aria-label="Portrait of a client with wavy auburn hair" style="left:21px;top:16px;width:124px;height:128px;background:linear-gradient(160deg,#e8ecef,#b47a4f 55%,#5d5a63)"></div>
      <p class="testimonial__quote" style="left:21px">“Lorem ipsum dolor sit<br>&nbsp;amet, consectetur adip<br>iscing elit, sed do eiusm ”</p>
    </article>
    <article class="testimonial" style="left:894px">
      <div class="testimonial__photo" role="img" aria-label="Portrait of a client in a suit" style="left:22px;top:15px;width:124px;height:128px;background:linear-gradient(160deg,#a9d3df,#d7a98a 55%,#1f2a44)"></div>
      <p class="testimonial__quote">“Lorem ipsum dolor sit<br>&nbsp;amet, consectetur adip<br>iscing elit, sed do eiusm ”</p>
    </article>

    <span class="testimonial__base" style="left:114px"></span>
    <span class="testimonial__base" style="left:362px"></span>
    <span class="testimonial__base" style="left:614px"></span>
    <span class="testimonial__base" style="left:869px"></span>
  </section>

  <section class="signup">
    <h3 class="signup__title">Get daily notes to motivate you everyday!</h3>
    <input class="signup__field" type="email" aria-label="Email address">
    <button class="signup__button" type="submit">SUBMIT</button>
  </section>
  <div class="signup__art" role="img" aria-label="Illustration of an envelope with a tick"></div>

  <footer class="site-footer">
    <h4 class="footer-heading" style="left:105px">MENU 1</h4>
    <ul class="footer-menu" style="left:106px"><li>Sub Menu</li><li>Sub menu</li><li>Sub Menu</li><li>Sub Menu</li><li>Sub Menu</li><li>Sub Menu</li></ul>
    <h4 class="footer-heading" style="left:253px">MENU 2</h4>
    <ul class="footer-menu" style="left:254px"><li>Sub Menu</li><li>Sub menu</li><li>Sub Menu</li><li>Sub Menu</li><li>Sub Menu</li><li>Sub Menu</li></ul>
    <h4 class="footer-heading" style="left:402px">MENU 3</h4>
    <ul class="footer-menu" style="left:403px"><li>Sub Menu</li><li>Sub menu</li><li>Sub Menu</li><li>Sub Menu</li><li>Sub Menu</li><li>Sub Menu</li></ul>

    <h4 class="footer-heading" style="left:630px;top:81px">CONNECT</h4>
    <ul class="social-links" aria-label="Social links">
      <li aria-label="Social link 1"></li><li aria-label="Social link 2"></li><li aria-label="Social link 3"></li><li aria-label="Social link 4"></li><li aria-label="Social link 5"></li>
    </ul>

    <h4 class="footer-heading" style="left:840px;width:282px;text-align:center">ROSS VALDANE</h4>
    <address class="contact">
      Textwerkstatt Nord<br>
      Lindenhofer Weg 42b<br>
      10117 Berlin<br>
      Germany<br>
      Telephone: +49 30 55501234<br>
      E-mail: hallo@textwerkstatt.example
    </address>
  </footer>
</body>
</html>
```